quorvaAgency Business Card Design Project

We need a business card design for quorvaAgency. quorvaAgency is an underwriting agency. Underwriting agencies act on behalf of insurers, to underwrite insurance. We will be operating in specialised classes of insurance initially and looking to expand from there. We would like to see designs that incorporate our logo colours as well as a contrasting stand out colour - also we'd like the logo itself to be embossed on the card.

Industry/Entity Type

Insurance

Requirements
Must have
• Logo on front
Nice to have
• Logo solely featured on back of card
Should not have
• Please do not use comic cans font :)

```html
<!DOCTYPE html>
<html lang="en">
<head>
<meta charset="utf-8">
<title>quorvaAgency Business Card</title>
<link href="https://fonts.googleapis.com/css2?family=Arimo:wght@700&family=Cabin:wght@400;500&family=Marcellus+SC&display=swap" rel="stylesheet">
<style>
  :root {
    --stage: #d8d9db;
    --paper: #ffffff;
    --navy-deep: #1d2c86;
    --navy: #0a4da1;
    --brand-blue: #124f9e;
    --label: #2b2b2b;
    --ink-light: #ffffff;
  }
  * { margin: 0; padding: 0; box-sizing: border-box; }
  html, body { width: 1200px; height: 601px; overflow: hidden; background: var(--stage); }
  .canvas { position: relative; width: 1200px; height: 601px; background: var(--stage); }
  .side-label {
    position: absolute; top: 86px; width: 200px; margin-left: -100px;
    text-align: center; font: 500 21px "Cabin", sans-serif; color: var(--label);
  }
  .card {
    position: absolute; top: 128px; width: 522px; height: 342px;
    background: var(--paper); border-radius: 40px; overflow: hidden;
  }
  .card--front { left: 63px; }
  .card--back { left: 616px; }
  .front-band {
    position: absolute; left: 0; top: 0; width: 100%; height: 224px;
    background: linear-gradient(180deg, var(--navy-deep) 0%, var(--navy) 100%);
  }
  .logo-seat {
    position: absolute; left: 209px; top: 156px; width: 104px; height: 104px;
    border-radius: 50%; background: var(--paper);
  }
  .holder-name {
    position: absolute; left: 38px; top: 46px;
    font: 400 27px "Marcellus SC", serif; color: var(--ink-light); letter-spacing: 0.5px;
  }
  .holder-role {
    position: absolute; left: 39px; top: 82px;
    font: 500 18px "Cabin", sans-serif; color: var(--ink-light);
  }
  .contact-list {
    position: absolute; left: 39px; top: 124px; list-style: none;
    font: 400 12px/15px "Cabin", sans-serif; color: var(--ink-light);
  }
  .wordmark {
    position: absolute; left: 0; width: 100%; text-align: center;
    font-family: "Arimo", sans-serif; font-weight: 700; color: var(--brand-blue);
    letter-spacing: -0.5px; white-space: nowrap;
  }
  .card--front .wordmark { top: 264px; font-size: 44px; }
  .brand-dot {
    position: absolute; left: 215px; top: 100px; width: 92px; height: 92px;
    border-radius: 50%; background: var(--brand-blue);
  }
  .card--back .wordmark { top: 196px; font-size: 54px; }
</style>
</head>
<body>
<main class="canvas">
  <p class="side-label" style="left:324px">front</p>
  <p class="side-label" style="left:877px">back</p>

  <section class="card card--front" aria-label="Card front">
    <div class="front-band"></div>
    <div class="logo-seat"></div>
    <h1 class="holder-name">Daniel Harlow</h1>
    <p class="holder-role">managing director</p>
    <ul class="contact-list">
      <li>A: 42 Wrenfield Ave, Halbrook, Canada</li>
      <li>P: 410 555 0192</li>
      <li>M: 077 555 2864</li>
      <li>E: hello@quorva-uw.com</li>
    </ul>
    <p class="wordmark">quorvaAgency</p>
  </section>

  <section class="card card--back" aria-label="Card back">
    <div class="brand-dot"></div>
    <p class="wordmark">quorvaAgency</p>
  </section>
</main>
</body>
</html>
```